CREATE A KILLER WEBSITE DESIGN

We are a firearms training company that trains CIVILIANS (no police or military pictures - thank you!) to defend themselves and are looking for a killer design that's clean, easy to navigate and modern! We want the newest trends applied to this sight like a scrollable site so you can scroll down and see all the features. We are okay with tweaking the HTML but need the artistic design to look good. I'll provide a link to our current site along with a sight we really like so you can get an idea!

I'm supplying a PowerPoint Design we are going with from another designer so you can match the style to the new site.

PAGES: (Please use information from our current site. We like the information but just want a more polished look similar to the NWDLA site below but in our colors.)
Home - Long Form Scrolling Site. Top fold will be a video with a play button.
Falcon Institute - Seven Level Training Program Info Page That Will Contain A Video.
Contact Us - This will be a page that DOES NOT CONTAIN AN EMAIL ADDRESS. Just a contact us form
Meet The Trainer: Morgan Pellbrook

Our site:
https://www.brisklanewardens.biz

Sights We Like:
https://www.nwdefenseleague.example.com
https://quorvel.example.com
https://brantforgeworks.example.com
https://www.pelnrigear.example.com

Target Market(s)

Men and women ages 21 to 100 years old

Industry/Entity Type

Self Defense

Number of Pages Required

5+ page

Font styles to use
Sans Serif

Colors
f26267

Requirements
Must have
• Clean and engaging. Use of colors that match our logo.
Should not have
• Poor design quality

```html
<!DOCTYPE html>
<html lang="en">
<head>
<meta charset="utf-8">
<title>Brisk Lane Wardens – Concealed Carry Training</title>
<link rel="stylesheet" href="https://fonts.googleapis.com/css2?family=Teko:wght@500;600&family=Fira+Sans:wght@400;500&display=swap">
<style>
:root{
  --red:#e5161d;
  --black:#0f0f0f;
  --dark:#151515;
  --header:#1c1c1c;
  --topbar:#252525;
  --footer:#1d1d1d;
  --copy:#141414;
  --white:#ffffff;
  --muted:#c9c9c9;
  --field:#4a4a4a;
  --head:'Teko',sans-serif;
  --body:'Fira Sans',sans-serif;
}
*{margin:0;padding:0;box-sizing:border-box}
html,body{width:1200px;height:2838px;overflow:hidden}
body{position:relative;background:var(--black);color:var(--white);font-family:var(--body)}
.abs{position:absolute}
.red{color:var(--red)}
.head{font-family:var(--head);font-weight:600;text-transform:uppercase;letter-spacing:.2px}

/* top bar */
.topbar{left:0;top:0;width:1200px;height:33px;background:var(--topbar)}
.topbar .phones{left:158px;top:8px;font-family:var(--head);font-size:15px;line-height:17px;display:flex;gap:8px;align-items:center}
.topbar svg{vertical-align:-1px;margin-right:3px}
.topbar .search{left:1021px;top:8px}

/* header */
.site-header{left:0;top:33px;width:1200px;height:123px;background:var(--header)}
.brand{left:158px;top:48px;width:135px;display:flex;flex-direction:column;align-items:center;gap:6px}
.brand .mark{width:34px;height:34px;border-radius:50%;border:3px solid var(--red)}
.brand .name{font-family:var(--head);font-weight:600;font-size:20px;line-height:18px;color:var(--red);text-align:center}
.header-actions{right:163px;top:61px;display:flex;gap:12px;align-items:center;font-family:var(--head);font-weight:500;font-size:14px}
.btn-sm{height:23px;padding:0 8px;line-height:25px;border-radius:2px}
.btn-sm.light{background:var(--white);color:#111}
.btn-sm.solid{background:var(--red);color:var(--white)}
.nav-rule{left:372px;top:108px;width:665px;height:2px;background:var(--red)}
.main-nav{left:372px;top:122px;width:665px;display:flex;justify-content:space-between;font-family:var(--head);font-weight:600;font-size:16px}

/* hero */
.hero{left:0;top:156px;width:1200px;height:434px;background:linear-gradient(120deg,#3b2a20 0%,#6a4a34 30%,#8a6546 55%,#4a3426 80%,#2e2019 100%)}
.hero-copy{left:158px;top:283px;width:370px;font-size:24px;line-height:32px}
.hero-buttons{left:158px;top:423px;display:flex;gap:24px}
.btn{height:33px;padding:0 10px;line-height:36px;font-family:var(--head);font-weight:600;font-size:19px}
.btn.light{background:var(--white);color:var(--red)}
.btn.solid{background:var(--red);color:var(--white)}
.hero-video{left:568px;top:235px;width:469px;height:274px;border:1px solid #ddd;background:linear-gradient(160deg,#6f8a4a 0%,#8ea46a 35%,#5e6b4c 65%,#3f4a34 100%)}
.hero-video .play{position:absolute;left:190px;top:103px}

/* about */
.portrait{left:509px;top:647px;width:182px;height:182px;border-radius:50%;border:3px solid var(--red);background:radial-gradient(circle at 50% 40%,#d6d6d6 0%,#8a8a8a 55%,#3a3a3a 100%)}
.about-label{left:0;top:851px;width:1200px;text-align:center;font-size:23px}
.about-name{left:0;top:872px;width:1200px;text-align:center;font-size:40px;color:var(--red)}
.about-copy{left:158px;top:920px;width:880px;font-size:14.6px;line-height:18px;text-align:center;letter-spacing:.4px}
.about-copy p+p{margin-top:18px}
.seen-title{left:0;top:1222px;width:1200px;text-align:center;font-size:36px}
.seen-logos{left:280px;top:1288px;width:640px;display:flex;justify-content:space-between;align-items:center;font-family:var(--head);font-weight:600;font-size:34px;line-height:40px}

/* training levels */
.levels{left:0;top:1422px;width:1200px;height:846px;background:linear-gradient(180deg,#3b4235 0%,#555a4d 30%,#4c4f45 60%,#36382f 100%)}
.levels-title{left:0;top:1460px;width:1200px;text-align:center;font-size:32px;line-height:38px}
.levels-copy{left:158px;top:1549px;width:882px;font-size:14.6px;line-height:18px;text-align:center;letter-spacing:.3px}
.levels-copy p+p{margin-top:18px}
.levels-copy u{font-weight:500}
.level{width:189px;height:232px;background:var(--black);border:2px solid #d8d8d8}
.level .num{position:absolute;left:0;top:30px;width:100%;text-align:center;font-family:var(--head);font-weight:600;font-size:118px;line-height:110px}
.level .tag{position:absolute;left:0;bottom:0;width:100%;height:47px;background:var(--red);display:flex;align-items:center;justify-content:center;text-align:center;font-family:var(--head);font-weight:600;font-size:17px;line-height:20px}

/* stories */
.stories{left:0;top:2268px;width:1200px;height:336px;background:var(--white);color:#111}
.stories-title{left:0;top:2326px;width:1200px;text-align:center;font-size:34px;color:#111}
.story-quote{left:285px;top:2399px;width:630px;text-align:center;font-size:19.5px;line-height:28.5px;color:#222;letter-spacing:.4px}
.story-rule{left:295px;top:2500px;width:611px;height:2px;background:var(--red)}
.story-name{left:0;top:2520px;width:1200px;text-align:center;font-size:19px;color:#222}
.story-date{left:0;top:2546px;width:1200px;text-align:center;font-size:15px;color:var(--red);letter-spacing:.6px}
.arrow{top:2393px}

/* footer */
.site-footer{left:0;top:2604px;width:1200px;height:195px;background:var(--footer)}
.foot-title{top:2620px;font-size:18px}
.foot-text{font-family:var(--head);font-weight:600;font-size:14px;line-height:22.5px}
.foot-divider{top:2625px;width:1px;height:155px;background:#444}
.contact-line{display:flex;gap:10px;align-items:flex-start}
.contact-line svg{margin-top:4px;flex:none}
.form-field{left:816px;width:221px;height:20px;background:var(--field);font-family:var(--head);font-weight:600;font-size:11px;line-height:22px;padding-left:11px;color:#ddd}
.copyright{left:0;top:2799px;width:1200px;height:39px;background:var(--copy);text-align:center;font-family:var(--head);font-weight:500;font-size:13px;line-height:42px;color:#aaa}
</style>
</head>
<body>

<div class="abs topbar">
  <div class="abs phones">
    <span><svg width="10" height="10" viewBox="0 0 10 10"><path d="M2 0l2 2-1 2c1 1 2 2 3 3l2-1 2 2-2 2C4 10 0 6 0 2z" fill="#e5161d"/></svg>LOCAL: 904-555-0142</span>
    <span><svg width="10" height="10" viewBox="0 0 10 10"><path d="M2 0l2 2-1 2c1 1 2 2 3 3l2-1 2 2-2 2C4 10 0 6 0 2z" fill="#e5161d"/></svg>TOLL-FREE: 800-555-0199</span>
  </div>
  <svg class="abs search" width="16" height="16" viewBox="0 0 16 16"><circle cx="6.5" cy="6.5" r="5" fill="none" stroke="#888" stroke-width="1.6"/><path d="M10 10l5 5" stroke="#888" stroke-width="1.8"/></svg>
</div>

<header class="abs site-header"></header>
<div class="abs brand">
  <span class="mark"></span>
  <span class="name">FALCON INSTITUTE</span>
</div>
<div class="abs header-actions">
  <span class="btn-sm light">JOIN FALCON INSTITUTE</span>
  <span class="btn-sm solid">I NEED IMMEDIATE SERVICE</span>
  <span><svg width="15" height="12" viewBox="0 0 15 12"><path d="M0 1h3l2 7h8l2-5H4" fill="none" stroke="#fff" stroke-width="1.6"/><circle cx="6" cy="10.5" r="1.3" fill="#fff"/><circle cx="12" cy="10.5" r="1.3" fill="#fff"/></svg> <span class="red">0</span></span>
  <span>LOG IN</span>
</div>
<div class="abs nav-rule"></div>
<nav class="abs main-nav">
  <span>HOME</span><span>FALCON INSTITUTE</span><span>TESTIMONIALS</span><span>ABOUT</span><span>UPCOMING CLASSES</span><span>SHOP</span><span>VIDEOS</span><span>LOST CERTIFICATE</span>
</nav>

<section class="abs hero" role="img" aria-label="Close-up photograph of a pistol resting in a leather holster beside brass cartridges"></section>
<h1 class="abs hero-copy head">Your life may depend on what you learn in your concealed carry training – <span class="red">don't settle for a gun shop class!</span></h1>
<div class="abs hero-buttons">
  <span class="btn light">FALCON INSTITUTE</span>
  <span class="btn solid">GET TICKETS NOW</span>
</div>
<div class="abs hero-video" role="img" aria-label="Video still of a hand holding a pistol over a mossy rock in the woods">
  <svg class="play" width="68" height="68" viewBox="0 0 68 68"><circle cx="34" cy="34" r="34" fill="#e5161d"/><path d="M26 19l25 15-25 15z" fill="#fff"/></svg>
</div>

<div class="abs portrait" role="img" aria-label="Black and white portrait of instructor Morgan Pellbrook"></div>
<h2 class="abs about-label head">About the Instructor</h2>
<h2 class="abs about-name head">Morgan Pellbrook</h2>
<div class="abs about-copy">
  <p>Morgan Pellbrook is a 3rd generation Cedar Hollow native and delighted to be a part of this great community. He is a true security expert with <span class="red">25 years of experience in the security industry.</span> He has appeared on <span class="red">Channel 7, Metro, KRT &amp; Daybreak</span> news outlets. He has been Featured in numerous publications and has <span class="red">trained thousands</span> to protect themselves and their homes from thugs and thieves. He is certified by both the <span class="red">NRSL</span> &amp; the <span class="red">NWDLA</span> as a firearms instructor. He is also an <span class="red">NRSL Range Safety Officer</span> and Defensive Pistol Instructor. He often says: "My students are like family so I take their security personal. I want them to feel confident that they can protect themselves and their families!"</p>
  <p>Brisk Lane Wardens is a <span class="red">radically different</span> concealed carry class focusing on the TRUTH about how "Real Attacks" take place. The Concealed Carry Class goes over way more than just the boring, lecture-style, gun shop curriculum into real strategies, tactics and training suggestions to help you prepare! You have to experience it to believe it! We also offer The <span class="red">Falcon Institute</span> for those who are looking for a <span class="red">Fully Immersive, Reality Based training environment that prepares you to defend against the worst threats you may face!</span> In The Institute, we utilize <span class="red">high tech,</span> military/law enforcement grade <span class="red">simulators to take training to a level never before seen in the world of concealed carry.</span></p>
</div>
<h2 class="abs seen-title head">As Seen On</h2>
<div class="abs seen-logos">
  <span>CHANNEL 7</span>
  <span>METRO</span>
  <span>KRT</span>
  <span>DAYBREAK</span>
</div>

<section class="abs levels" role="img" aria-label="Photograph of a pistol lying on a weathered log in the forest"></section>
<h2 class="abs levels-title head">Our 7 levels of training take you<br>from zero to hero</h2>
<div class="abs levels-copy">
  <p>Wanna hear something funny? Guess what the average person asks about a concealed weapons class? "How much is it and how long is it?" Can you believe it? We are talking about preparing you for life and death situations and the main concern is "How Fast" and "How Cheap?" WOW!</p>
  <p>Why do <u>most people settle for a cheap &amp; quick concealed carry class?</u> It's a fair question! Could you imagine a military soldier trained by a 2-hour class? How effective would they be in the heat of battle? If you want to be ready to SURVIVE an attack, <u>YOU NEED MORE</u> than a basic, run of the mill class! That's why we created a <u>PROPRIETARY 7 LEVEL TRAINING SYSTEM</u> to take you all the way to the peak of readiness!</p>
</div>

<div class="abs level" style="left:158px;top:1738px"><div class="num">1</div><div class="tag">CONCEALED CARRY<br>CLASS</div></div>
<div class="abs level" style="left:388px;top:1738px"><div class="num">2</div><div class="tag">DYNAMIC DEFENSIVE<br>SHOOTING</div></div>
<div class="abs level" style="left:618px;top:1738px"><div class="num">3</div><div class="tag">FINE TUNING YOUR<br>TECHNIQUE</div></div>
<div class="abs level" style="left:848px;top:1738px"><div class="num">4</div><div class="tag">VIRTUAL<br>THREAT-LAB</div></div>
<div class="abs level" style="left:273px;top:2008px"><div class="num">5</div><div class="tag">TACTICAL SKILLS &amp;<br>DRILLS</div></div>
<div class="abs level" style="left:504px;top:2008px"><div class="num">6</div><div class="tag">CLOSE QUARTERS<br>DEFENSE</div></div>
<div class="abs level" style="left:735px;top:2008px"><div class="num">7</div><div class="tag">LIVE SCENARIO<br>THREAT-LAB</div></div>

<section class="abs stories"></section>
<h2 class="abs stories-title head">Success Stories</h2>
<svg class="abs arrow" style="left:158px" width="37" height="54" viewBox="0 0 37 54"><path d="M37 0v54L0 27z" fill="#111"/></svg>
<svg class="abs arrow" style="left:999px" width="37" height="54" viewBox="0 0 37 54"><path d="M0 0v54l37-27z" fill="#111"/></svg>
<p class="abs story-quote">"I had never held a gun when I took the Brisk Lane Wardens class and I'm hooked! I'm going all the way to level 7! Thank you Brisk Lane Wardens!"</p>
<div class="abs story-rule"></div>
<p class="abs story-name">Dana R.</p>
<p class="abs story-date">October 14, 2017</p>

<footer class="abs site-footer"></footer>
<h3 class="abs foot-title head" style="left:158px">Morgan Pellbrook</h3>
<p class="abs foot-text" style="left:158px;top:2652px;width:220px">NRSL FIREARMS INSTRUCTOR, NWDLA INSTRUCTOR &amp; TRAINING COUNSELLOR, NEWS CORRESPONDENT, AND SECURITY EXPERT</p>
<div class="abs foot-divider" style="left:417px"></div>
<h3 class="abs foot-title head" style="left:466px">Contact Us</h3>
<div class="abs foot-text" style="left:466px;top:2652px">
  <div class="contact-line"><svg width="10" height="13" viewBox="0 0 10 13"><path d="M5 0a5 5 0 015 5c0 3-5 8-5 8S0 8 0 5a5 5 0 015-5z" fill="#e5161d"/><circle cx="5" cy="5" r="1.8" fill="#1d1d1d"/></svg><span>P.O. BOX 4410<br>CEDAR HOLLOW, FL 32999</span></div>
  <div class="contact-line" style="margin-top:18px"><svg width="10" height="10" viewBox="0 0 10 10"><path d="M2 0l2 2-1 2c1 1 2 2 3 3l2-1 2 2-2 2C4 10 0 6 0 2z" fill="#e5161d"/></svg><span>LOCAL: 904-555-0142</span></div>
  <div class="contact-line"><svg width="10" height="10" viewBox="0 0 10 10"><path d="M2 0l2 2-1 2c1 1 2 2 3 3l2-1 2 2-2 2C4 10 0 6 0 2z" fill="#e5161d"/></svg><span>TOLL-FREE: 800-555-0199</span></div>
  <div class="contact-line"><svg width="12" height="9" viewBox="0 0 12 9"><rect width="12" height="9" fill="#e5161d"/><path d="M0 0l6 5 6-5" fill="none" stroke="#1d1d1d" stroke-width="1.2"/></svg><span>INFO@BRISKLANEWARDENS.EXAMPLE.COM</span></div>
</div>
<div class="abs foot-divider" style="left:758px"></div>
<h3 class="abs foot-title head" style="left:816px;width:221px;text-align:right">Get in Touch</h3>
<div class="abs form-field" style="top:2647px">NAME</div>
<div class="abs form-field" style="top:2675px">EMAIL</div>
<div class="abs form-field" style="top:2704px">PHONE</div>
<div class="abs form-field" style="top:2733px;height:47px">MESSAGE</div>
<div class="abs copyright">COPYRIGHT BRISK LANE WARDENS 2020 – ALL RIGHTS RESERVED</div>

</body>
</html>
```